Brindle Market is an online marketing platform.

A daily deals site for consumers a way to bring in new clients for clients and this is who the business cards are for. Industries - Food and Drink, Things To Do, Beauty and Spas, Staycations and Services.
Logo on one side.
Name - Owen Carradine
Job Title - Sales Director
Phone Number - 07912583046
Email - owen@brindlemarket.co.uk
need same for second person
Name - Tessa Lindqvist
Job Title - Operations Director
Phone Number - 01632884275
Email - tessa@brindlemarket.co.uk
Bottom Right - Facebook Icon, Insta Icon, Twitter Icon
Target Market(s)
Business owners of the above industries
Contact Information for Business Card
Name - Owen Carradine
Name - Tessa Lindqvist
Look and feel
Each slider illustrates characteristics of the customer's brand and the style your logo design should communicate.

```html
<!DOCTYPE html>
<html lang="en">
<head>
<meta charset="utf-8">
<title>Brindle Market – Business Card</title>
<link rel="stylesheet" href="https://fonts.googleapis.com/css2?family=Open+Sans:wght@400;700&display=swap">
<style>
  :root {
    --page-bg: #d9d4cc;
    --card-bg: #eeedea;
    --card-edge: #f8f8f6;
    --brand-navy: #1d5283;
    --ink-dark: #3a3a3c;
    --ink-mid: #57585a;
  }
  * { margin: 0; padding: 0; box-sizing: border-box; }
  html, body {
    width: 1200px;
    height: 1200px;
    overflow: hidden;
    background: var(--page-bg);
    font-family: "Open Sans", sans-serif;
  }
  .canvas {
    position: relative;
    width: 1200px;
    height: 1200px;
  }
  .business-card {
    position: absolute;
    left: 80px;
    top: 315px;
    width: 1040px;
    height: 570px;
    background: var(--card-bg);
    border: 2px solid var(--card-edge);
    border-radius: 22px;
  }
  .brand-lockup {
    position: absolute;
    left: 58px;
    top: 92px;
    display: flex;
    align-items: center;
    gap: 16px;
  }
  .brand-mark {
    width: 92px;
    height: 92px;
    border-radius: 50%;
    border: 7px solid var(--brand-navy);
  }
  .brand-name {
    font-weight: 700;
    font-size: 50px;
    letter-spacing: 0.5px;
    color: var(--brand-navy);
    line-height: 1;
  }
  .contact-person {
    position: absolute;
    left: 58px;
    top: 290px;
  }
  .person-name {
    font-weight: 700;
    font-size: 36px;
    letter-spacing: 0.5px;
    color: var(--brand-navy);
    text-transform: uppercase;
    line-height: 1.1;
  }
  .person-role {
    margin-top: 8px;
    font-weight: 400;
    font-size: 27px;
    color: var(--ink-mid);
  }
  .contact-list {
    position: absolute;
    left: 58px;
    top: 430px;
    list-style: none;
  }
  .contact-item {
    display: flex;
    align-items: center;
    gap: 12px;
    font-size: 27px;
    color: var(--ink-mid);
    line-height: 38px;
  }
  .contact-icon {
    width: 22px;
    height: 22px;
    fill: var(--brand-navy);
    flex: none;
  }
  .feature-mark {
    position: absolute;
    left: 600px;
    top: 30px;
    width: 400px;
    height: 400px;
    border-radius: 50%;
    border: 10px solid var(--brand-navy);
    display: flex;
    align-items: center;
    justify-content: center;
    text-align: center;
  }
  .feature-name {
    font-weight: 700;
    font-size: 58px;
    line-height: 1.1;
    color: var(--ink-dark);
  }
  .social-links {
    position: absolute;
    left: 880px;
    top: 477px;
    display: flex;
    gap: 10px;
  }
  .social-tile {
    width: 21px;
    height: 21px;
    border-radius: 4px;
    background: var(--brand-navy);
  }
</style>
</head>
<body>
<main class="canvas">
  <section class="business-card">
    <div class="brand-lockup">
      <span class="brand-mark"></span>
      <span class="brand-name">Brindle Market</span>
    </div>

    <div class="contact-person">
      <h1 class="person-name">Owen Carradine</h1>
      <p class="person-role">Sales Director</p>
    </div>

    <ul class="contact-list">
      <li class="contact-item">
        <svg class="contact-icon" viewBox="0 0 24 24" aria-hidden="true"><path d="M6.6 10.8a15.1 15.1 0 0 0 6.6 6.6l2.2-2.2a1 1 0 0 1 1-.25 11.4 11.4 0 0 0 3.6.57 1 1 0 0 1 1 1V20a1 1 0 0 1-1 1A17 17 0 0 1 3 4a1 1 0 0 1 1-1h3.5a1 1 0 0 1 1 1c0 1.25.2 2.45.57 3.57a1 1 0 0 1-.25 1z"/></svg>
        <span>07912583046</span>
      </li>
      <li class="contact-item">
        <svg class="contact-icon" viewBox="0 0 24 24" aria-hidden="true"><path d="M2 5h20v2l-10 6L2 7z M2 9l10 6 10-6v10H2z"/></svg>
        <span>owen@brindlemarket.co.uk</span>
      </li>
    </ul>

    <div class="feature-mark">
      <span class="feature-name">Brindle<br>Market</span>
    </div>

    <div class="social-links">
      <span class="social-tile"></span>
      <span class="social-tile"></span>
      <span class="social-tile"></span>
      <span class="social-tile"></span>
    </div>
  </section>
</main>
</body>
</html>
```